Natural Handmade Cosmetics Line

I'm looking for a range of labels for a natural handmade Cosmetics company in UK. I'm looking to print the labels on a transparent substrate. The ingredients & Details are on the website. Varenta means Lovely or beloved in latin. The products are designed & manufactured by hand but I want to give the impression of a high end cosmetic brand.

I would like a tag line of some description like "Natural, Pure, Handmade" included

The name of the company is varenta cosmetics (www.varenta.co.uk) and I have the following products (All skin types)

1. Orange & Rose Toner - 150ml (Length: 14cm / hight 9.5cm)
2. Grapefruit Cleanser - 150g (Length 14cm / Hight 9.5cm)
3. Balancing Facial Oil - 30ml (Length 10.5cm / Hight 4.6cm)
4. Frankincense & Neroli Facial Oil - 30ml (Length 10.5cm / Hight 4.6cm)
5. Neroli Moisturizing Face Cream - 50g (Length 15cm / Hight 5cm)
6. Lavender & Neroli Hand Cream - 100g (Length 15cm / Hight 8cm)
7. Tangerine Lip Balm - 4g (Length 5.4cm / Hight 4.6cm) - Lip Balm Tube
8. Mandarin Treatment Balm 50g (Length16.4cm / Hight 3.1cm)
9. Lemon & Tangerine Body Butter - 100g (Length 29cm / Hight 2.5cm)
10. Ylang Ylang & Bergamot Body Butter - 100g (Length 29cm / Hight 2.5cm)

Ideally in the future I would like to get some boxes designed.

I like the following designs

https://www.trumolia.co.uk/face/range/product-family/daily-essentials/
http://www.skyfoxten.co.uk/shop-for-products/natural-skin-care/organic-moisturiser-products
http://www.kuvaderm.com/
http://www.lumaderm.com/
http://www.thebrightmeadowcompany.co.uk/organic-natural-skincare/dry-sensitive/lumaderm-daily-moisture-for-men.html

Dimensions altered

Target Market(s)

Targeting woman of 25+

Industry/Entity Type

Cosmetics

Requirements
Must have
• The correct symbols which are included

```html
<!DOCTYPE html>
<html lang="en">
<head>
<meta charset="utf-8">
<title>Varenta Cosmetics – Label Range</title>
<link rel="stylesheet" href="https://fonts.googleapis.com/css2?family=Roboto+Slab:wght@400;700&family=Open+Sans:ital,wght@0,400;1,400&display=swap">
<style>
  :root {
    --paper: #ffffff;
    --ink: #111111;
    --body-ink: #1c1c1c;
    --tagline: #8a8a8a;
    --rule: #222222;
    --frame: #333333;
    --art: #ececec;
    --shadow: rgba(0, 0, 0, 0.45);
  }
  * { box-sizing: border-box; margin: 0; padding: 0; }
  html, body { width: 1200px; height: 783px; overflow: hidden; background: var(--paper); }
  .sheet { position: relative; width: 1200px; height: 783px; }

  .label {
    position: absolute;
    background: var(--paper);
    border: 1px solid var(--frame);
    box-shadow: 9px 13px 9px var(--shadow);
  }
  .label > * { position: absolute; }

  .label__art { background: radial-gradient(ellipse at center, #e4e4e4 0%, var(--art) 55%, rgba(236,236,236,0) 100%); }

  .brand {
    font-family: "Roboto Slab", serif;
    font-weight: 400;
    color: var(--ink);
    line-height: 1;
    letter-spacing: -0.5px;
  }
  .tagline {
    font-family: "Open Sans", sans-serif;
    font-style: italic;
    color: var(--tagline);
    white-space: nowrap;
    line-height: 1;
  }
  .tagline--vertical { transform-origin: left top; transform: rotate(-90deg); }
  .rule { height: 1px; background: var(--rule); }
  .product-name {
    font-family: "Roboto Slab", serif;
    font-weight: 700;
    color: var(--ink);
    white-space: nowrap;
    line-height: 1;
  }
  .description {
    font-family: "Open Sans", sans-serif;
    color: var(--body-ink);
  }

  /* Tangerine lip balm */
  .label--lip { left: 476px; top: 0; width: 218px; height: 186px; }
  .label--lip .label__art { left: 548px; left: 70px; top: 108px; width: 120px; height: 74px; }
  .label--lip .tagline { left: 19px; top: 136px; font-size: 10px; }
  .label--lip .brand { left: 35px; top: 9px; font-size: 22px; }
  .label--lip .rule { left: 35px; top: 38px; width: 177px; }
  .label--lip .product-name { left: 37px; top: 50px; font-size: 15.5px; }
  .label--lip .description { left: 37px; top: 90px; width: 176px; font-size: 7.1px; line-height: 9.1px; }

  /* Mandarin treatment balm */
  .label--balm { left: 276px; top: 272px; width: 663px; height: 126px; }
  .label--balm .label__art { left: 95px; top: 6px; width: 130px; height: 110px; }
  .label--balm .tagline { left: 213px; top: 120px; font-size: 10.5px; }
  .label--balm .brand { left: 229px; top: 10px; font-size: 23px; }
  .label--balm .rule { left: 229px; top: 41px; width: 210px; }
  .label--balm .product-name { left: 229px; top: 46px; font-size: 17px; }
  .label--balm .description { left: 231px; top: 69px; width: 432px; font-size: 8.6px; line-height: 11.8px; }

  /* Body butters */
  .label--butter-lemon { left: 0; top: 493px; width: 1173px; height: 102px; }
  .label--butter-ylang { left: 8px; top: 656px; width: 1174px; height: 102px; }
  .label--butter-lemon .label__art { left: 205px; top: 8px; width: 172px; height: 82px; }
  .label--butter-ylang .label__art { left: 254px; top: 8px; width: 160px; height: 82px; }
  .label--butter-lemon .brand { left: 383px; top: 12px; font-size: 22px; }
  .label--butter-ylang .brand { left: 428px; top: 9px; font-size: 22px; }
  .label--butter-lemon .tagline--inline { left: 473px; top: 21px; font-size: 9px; }
  .label--butter-ylang .tagline--inline { left: 520px; top: 18px; font-size: 9px; }
  .label--butter-lemon .rule { left: 383px; top: 44px; width: 257px; }
  .label--butter-ylang .rule { left: 428px; top: 39px; width: 299px; }
  .label--butter-lemon .product-name { left: 383px; top: 51px; font-size: 15px; }
  .label--butter-ylang .product-name { left: 429px; top: 50px; font-size: 15.5px; }
  .label--butter-lemon .description { left: 794px; top: 20px; width: 376px; font-size: 7px; line-height: 10.4px; }
  .label--butter-ylang .description { left: 771px; top: 18px; width: 396px; font-size: 7px; line-height: 10.4px; }
</style>
</head>
<body>
<main class="sheet">

  <section class="label label--lip">
    <div class="label__art" role="img" aria-label="Faint line illustration of a tangerine"></div>
    <span class="tagline tagline--vertical">Natural, Pure, Handmade</span>
    <span class="brand">Varenta</span>
    <div class="rule"></div>
    <h2 class="product-name">Tangerine Lip Balm</h2>
    <p class="description">This is our most popular product and we have some very positive feedback from many satisfied customers. Used daily, this natural treatment balm can help to soften hard skin on the feet, elbows, knees &amp; hands. It also helps moisturise dry areas of skin. Works on all skin types and people with problem dry skin areas on the body.</p>
  </section>

  <section class="label label--balm">
    <div class="label__art" role="img" aria-label="Faint line illustration of a mandarin with leaves"></div>
    <span class="tagline tagline--vertical">Natural, Pure, Handmade</span>
    <span class="brand">Varenta</span>
    <div class="rule"></div>
    <h2 class="product-name">Mandarin Treatment Balm</h2>
    <p class="description">This is our most popular product and we have some very positive feedback from many satisfied customers. Used daily, this natural treatment balm can help to soften hard skin on the feet, elbows, knees &amp; hands. It also helps moisturise dry areas of skin. Works on all skin types and people with problem dry skin areas on the body.</p>
  </section>

  <section class="label label--butter-lemon">
    <div class="label__art" role="img" aria-label="Faint line illustration of lemons and tangerines"></div>
    <span class="brand">Varenta</span>
    <span class="tagline tagline--inline">Natural, Pure, Handmade</span>
    <div class="rule"></div>
    <h2 class="product-name">Lemon &amp; Tangerine Body Butter</h2>
    <p class="description">Our rich Lemon &amp; Tangerine, light, fluffy textured luscious body butter for the hydration and nourishment of your skin. Melts upon contact with your skin. With a blend of mango butter and Sunflower &amp; Jojoba Oils for extra vitamins and anti-oxidants. Evening primrose oil is included and penetrates down and into the skin, which as a result becomes softer and has a moisture-retaining effect, prevents drying of the skin, increases the cells’ ability to absorb oxygen<br>PLEASE NOTE: This body butter does not contain water and therefore extremely rich.</p>
  </section>

  <section class="label label--butter-ylang">
    <div class="label__art" role="img" aria-label="Faint line illustration of bergamot fruit and ylang ylang flowers"></div>
    <span class="brand">Varenta</span>
    <span class="tagline tagline--inline">Natural, Pure, Handmade</span>
    <div class="rule"></div>
    <h2 class="product-name">Ylang Ylang &amp; Bergamot Body Butter</h2>
    <p class="description">Our rich Ylang Ylang &amp; Bergamot, light, fluffy textured luscious body butter for the hydration and nourishment of your skin. Melts upon contact with your skin. With a blend of mango butter and Sunflower &amp; Jojoba Oils for extra vitamins and anti-oxidants. Evening primrose oil is included and penetrates down and into the skin, which as a result becomes softer and has a moisture-retaining effect, prevents drying of the skin, increases the cells’ ability to absorb oxygen<br>PLEASE NOTE: This body butter does not contain water and therefore extremely rich.</p>
  </section>

</main>
</body>
</html>
```